Business card for Drone Aerial

I need a business card designed keeping in mind I want to do post cards also with a similar design.
Both sides of the card would be cool.
I have a skylark 5 max and would like a picture of it on the front of the card. Similar to one I attached.
I really like the look of a drone in the air and the background pic a little blurry. I attached a few images as IDEAS.
Some special things I want to be on the card additional to the normal business card info:
"Aerial Photography" or "Low Altitude Aerial Photography"?
"ZQB# 90817263"

I like modern and creative. My Favorite color is blue and I like blue on white.
I do not have a business name and am not going to have one. When they read "Aerial Photography" and see the drone and image they will know what the card is for.

FYI, The attached pictures are just images from framewillow and just samples/ideas.

Target Market(s)

Real estate, construction, events

Industry/Entity Type

Business

Contact Information for Business Card

Also Definitely want to contain, my name, my number and email address.

Requirements
Must have
• "ZQB# 90817263"
• "Aerial Photography"

```html
<!DOCTYPE html>
<html lang="en">
<head>
<meta charset="utf-8">
<title>Aerial Photography – Business Card</title>
<link rel="stylesheet" href="https://fonts.googleapis.com/css2?family=Exo+2:wght@700&family=Open+Sans:wght@400;700&display=swap">
<style>
  :root{
    --page:#f1f1f1;
    --band:#3a4ea0;
    --white:#ffffff;
    --forest-dark:#3e3a2a;
    --forest-mid:#6d7a48;
    --forest-light:#8e9a62;
    --sky:#a9b7d6;
    --town:#8d8fa0;
    --town-dark:#4c4f5c;
  }
  html,body{margin:0;padding:0;}
  body{width:1200px;height:1119px;overflow:hidden;background:var(--page);position:relative;}
  .card{position:absolute;width:693px;height:396px;overflow:hidden;box-shadow:0 4px 14px rgba(0,0,0,.18);}
  .card--front{left:348px;top:122px;}
  .card--back{left:200px;top:600px;}
  .photo{position:absolute;inset:0;}
  .card--front .photo{
    background:
      radial-gradient(ellipse 190px 150px at 52% 50%, rgba(240,240,240,.85), rgba(240,240,240,0) 70%),
      linear-gradient(180deg,var(--forest-dark) 0%,var(--forest-mid) 55%,var(--forest-light) 100%);
  }
  .card--back .photo{
    background:
      radial-gradient(ellipse 170px 120px at 62% 48%, rgba(245,245,248,.9), rgba(245,245,248,0) 70%),
      linear-gradient(180deg,var(--sky) 0%,#b9c2da 35%,var(--town) 62%,var(--town-dark) 100%);
  }
  .title-band{position:absolute;background:var(--band);color:var(--white);text-align:center;
    display:flex;flex-direction:column;justify-content:center;align-items:center;}
  .card--front .title-band{left:442px;top:207px;width:251px;height:76px;}
  .card--back .title-band{left:0;top:139px;width:278px;height:76px;}
  .title-band__main{font-family:"Exo 2",sans-serif;font-weight:700;font-size:44px;line-height:40px;letter-spacing:1px;}
  .title-band__sub{font-family:"Open Sans",sans-serif;font-weight:700;font-size:18px;line-height:20px;letter-spacing:1px;}
  .owner{position:absolute;left:0;width:316px;text-align:center;color:var(--white);font-family:"Open Sans",sans-serif;}
  .owner__name{top:26px;font-weight:700;font-size:26px;line-height:30px;}
  .owner__licence{top:56px;font-size:15px;line-height:20px;}
  .contact{position:absolute;left:0;top:234px;width:316px;text-align:center;color:var(--white);
    font-family:"Open Sans",sans-serif;font-size:16px;line-height:22px;margin:0;padding:0;list-style:none;}
</style>
</head>
<body>
  <section class="card card--front">
    <div class="photo" role="img" aria-label="White quadcopter drone hovering in front of a blurred green forest"></div>
    <div class="title-band">
      <span class="title-band__main">Aerial</span>
      <span class="title-band__sub">PHOTOGRAPHY</span>
    </div>
  </section>

  <section class="card card--back">
    <div class="photo" role="img" aria-label="White quadcopter drone flying above a blurred town under a pale blue sky"></div>
    <div class="owner owner__name">Mara Lindqvist</div>
    <div class="owner owner__licence">ZQB# 90817263</div>
    <div class="title-band">
      <span class="title-band__main">Aerial</span>
      <span class="title-band__sub">PHOTOGRAPHY</span>
    </div>
    <ul class="contact">
      <li>#47, Heron Lane</li>
      <li>Brookfield, Norland</li>
      <li>P: 482.310.7745</li>
      <li>C: 482.619.2083</li>
      <li>E: hello@maraskyview.com</li>
      <li>www.maraskyview.com</li>
    </ul>
  </section>
</body>
</html>
```